Website created on Plinkora.com

I have a telecommunications company and i would like my website built on plinkora.com as this platform is easy for me to change in the future so the site needs to be made so i can change it when i need to. Also I have found Plinkora is very good for SEO setup
Examples of websites i like as they are clean and corporate www.tarnocall.com.au (on this site there are menus on the right hand side which changes the content on the same page I would like the also www.quelbiline.com.au
My company sells business phone systems we sell the following products
1. Hosted PBX (This is the main product/service we sell)
2. Dorvex products (Dorvex has a range of products Phone systems, Gateways and Software we sell all products)
3. Pranmoor Phones (we sell the following Pranmoor phones T46G, T42G, T41G, T28P, T26P, T22P, T20P, VP530, W52P, EXP39, EXP40
4. KelSwitch (www.lumbrakt.com) we sell SoHo and all the U series plus the add on's
5. VoIP plans (this is a outbound phone service for business customer)
1. business starter ($0 month 0 call included .12c local calls .24c mobile calls
2. business saver ($25 month 250 local calls included .10c local calls .22c mobile calls
3. business super ($50 month 500 local calls included .09c local calls .20c mobile calls
4. business extreme ($100 month 1000 local calls included .08c local calls .18c mobile calls
home page
custom corporate banners for each product/service 1. Hosted PBX 2. VoIP Plans 3. Pranmoor Phones 4. KelSwitch 5. Dorvex, Which will rotate every 4 seconds
next will be displaying the VoIP plans with links to the plans pages
next icons of 1. Hosted PBX, 2. Pranmoor phones 3. KelSwitch 4. Dorvex with links to the right page within the site
next a section with a description and design of what the business can do you the customer, please give me some examples
Product pages for all products/services Hosted PBX, Pranmoor, KelSwitch, Dorvex and VoIP plans
Please make a pages for Headsets and I will attached the brands later
The aim is to have a clean white corporate website that ranks very will in fandrix that I can manage in the future
Please do not copy my existing site
small to medium business
Telecommunications

```html
<!DOCTYPE html>
<html lang="en">
<head>
<meta charset="utf-8">
<title>Tellaro Voice – Business Phone Systems</title>
<link href="https://fonts.googleapis.com/css2?family=Open+Sans:wght@400;600;700&display=swap" rel="stylesheet">
<style>
:root{
  --ink:#333;
  --muted:#666;
  --blue:#1a62a8;
  --navy:#0d4a8a;
  --line:#e3e3e3;
  --btn:#8a8c8f;
  --dark:#333;
}
*{margin:0;padding:0;box-sizing:border-box}
html,body{width:920px;height:1200px;overflow:hidden;background:#fff}
body{position:relative;font-family:'Open Sans',sans-serif;color:var(--ink)}
.abs{position:absolute}
.brand{left:78px;top:36px;font-size:26px;font-weight:700;color:var(--navy);letter-spacing:-.5px;display:flex;align-items:center;gap:8px}
.brand i{display:block;width:14px;height:14px;border-radius:50%;background:var(--navy)}
.top-nav{left:480px;top:24px;font-size:10.5px;color:#555;display:flex;gap:8px}
.top-nav span.sep{color:#bbb}
.call{left:694px;top:16px;width:150px;height:32px;border-left:1px solid #ddd;text-align:right}
.call small{display:block;font-size:11px;color:#444;margin-right:34px}
.call strong{display:block;font-size:16px;font-weight:600;color:#222;margin-right:34px;line-height:18px}
.call svg{position:absolute;right:4px;top:4px}
.rule-top{left:477px;top:61px;width:367px;height:1px;background:#e6e6e6}
.nav-item{top:76px;font-size:11.2px;color:#333;white-space:nowrap}
.nav-item.on{color:var(--blue)}
.nav-item::before{content:"• "}
.hero{left:76px;top:112px;width:768px;height:296px;background:#e6e6e6;padding:6px}
.hero-inner{width:100%;height:100%;background:linear-gradient(100deg,#fff 0%,#fff 60%,#ececec 100%);position:relative}
.hero h1{position:absolute;left:30px;top:62px;font-size:19px;font-weight:400;line-height:24px;color:#222}
.hero p{position:absolute;left:32px;top:117px;width:320px;font-size:10.4px;line-height:16px;color:#333}
.hero .btn{position:absolute;left:32px;top:176px;width:76px;height:25px;background:#777;color:#fff;font-size:11px;line-height:25px;text-align:center;border-radius:2px}
.hero .dots{position:absolute;left:28px;top:262px;display:flex;gap:8px}
.hero .dots b{width:10px;height:10px;border-radius:50%;background:#aaa;display:block}
.hero .dots b:first-child{background:#666}
.hero .photo{position:absolute;left:402px;top:42px;width:248px;height:216px;border-radius:10px;background:linear-gradient(160deg,#6e7073,#2d2f31)}
.plan{top:433px;width:176px;height:205px;border:1px solid #e4e4e4;background:linear-gradient(#fff 60%,#f4f4f4);text-align:center}
.plan h2{margin:4px 4px 0;height:29px;background:linear-gradient(#1b6bb5,#0b4787);color:#fff;font-size:14px;font-weight:700;line-height:29px;border-radius:2px}
.plan .price{margin:22px 18px 0;height:42px;font-size:29px;color:var(--blue);font-weight:400;line-height:40px;border-bottom:1px solid #eee}
.plan .price small{font-size:11px;color:#555}
.plan ul{list-style:none;margin:0 18px}
.plan li{height:27px;line-height:27px;font-size:12px;color:#444;border-bottom:1px solid #f0f0f0}
.plan li:last-child{border:0}
.plan .sign{position:absolute;left:30px;top:187px;width:117px;height:29px;background:linear-gradient(#9a9c9f,#7b7d80);color:#fff;font-size:13px;font-weight:600;line-height:29px;border-radius:2px;box-shadow:0 6px 8px -4px rgba(0,0,0,.3)}
.features{left:76px;top:688px;width:768px;height:104px;border-top:1px solid #e3e3e3;border-bottom:1px solid #e3e3e3;display:flex;padding:14px 0}
.feature{flex:1;text-align:center;border-left:1px solid #e3e3e3;position:relative}
.feature:first-child{border-left:0}
.feature .ic{height:46px;display:flex;align-items:center;justify-content:center}
.feature h3{font-size:13.6px;font-weight:700;color:#111;margin-top:4px}
.feature .wordmark{font-size:26px;color:#444;font-weight:400;letter-spacing:1px}
.about h2{position:absolute;left:86px;top:830px;font-size:16px;font-weight:700;color:var(--blue)}
.about p{position:absolute;left:86px;top:860px;width:598px;font-size:10.4px;line-height:17.6px;color:#333}
.about .art{position:absolute;left:696px;top:816px;width:136px;height:132px;border-radius:50%;background:radial-gradient(circle,#cfe1f3,#eef3f8 70%,#fff)}
.band{left:76px;top:970px;width:768px;height:8px;background:repeating-linear-gradient(45deg,#ddd 0 2px,#f2f2f2 2px 4px)}
.fcol h4{font-size:12px;font-weight:700;color:#222;margin-bottom:6px}
.fcol ul{list-style:none}
.fcol li{font-size:10.4px;line-height:17.6px;color:#555;padding-left:12px;position:relative}
.fcol li::before{content:"•";position:absolute;left:0;color:#888}
.social{display:flex;gap:5px;background:#eee;padding:4px;width:146px;margin:9px 0 8px -2px}
.social b{width:22px;height:22px;border-radius:50%;background:#8e9093;display:block}
.contact{font-size:10.4px;line-height:17.6px;color:#555}
.foot{left:0;top:1160px;width:920px;height:40px;background:var(--dark);color:#bbb;font-size:10.4px;text-align:center;line-height:40px}
</style>
</head>
<body>

<header>
  <div class="abs brand"><i></i>Tellaro Voice</div>
  <nav class="abs top-nav"><span>Home</span><span class="sep">/</span><span>About</span><span class="sep">/</span><span>Contact Us</span><span class="sep">/</span><span>Signin</span></nav>
  <div class="abs call">
    <small>Call us now!</small>
    <strong>1300 482 917</strong>
    <svg width="22" height="20" viewBox="0 0 24 24"><path d="M6.6 10.8c1.4 2.8 3.8 5.1 6.6 6.6l2.2-2.2c.3-.3.7-.4 1-.2 1.1.4 2.3.6 3.6.6.6 0 1 .4 1 1V20c0 .6-.4 1-1 1C10.6 21 3 13.4 3 4c0-.6.4-1 1-1h3.5c.6 0 1 .4 1 1 0 1.3.2 2.5.6 3.6.1.3 0 .7-.2 1z" fill="#333" transform="rotate(20 12 12)"/></svg>
  </div>
  <div class="abs rule-top"></div>
  <nav>
    <span class="abs nav-item on" style="left:477px">Products</span>
    <span class="abs nav-item" style="left:550px">Hosted PBX</span>
    <span class="abs nav-item" style="left:634px">Telephone Systems</span>
    <span class="abs nav-item" style="left:758px">Plans &amp; Signup</span>
  </nav>
</header>

<section class="abs hero">
  <div class="hero-inner">
    <h1>VOIP<br>consectetur consectetur</h1>
    <p>Donec eu tempus risus. Nulla accumsan lacus nec rutrum aliquet. Nam quis suscipit ligula. Interdum et malesuada fames ac ante ipsum primis in fauci bus tincidunt velit commodo</p>
    <div class="btn">Read more</div>
    <div class="dots"><b></b><b></b><b></b><b></b></div>
    <div class="photo" role="img" aria-label="Photo of a grey IP desk telephone with handset and display"></div>
  </div>
</section>

<section class="plans">
  <div class="abs plan" style="left:85px"><h2>BUSINESS STARTER</h2><div class="price">$0<small> / month</small></div><ul><li>0 call included</li><li>.12c local calls</li><li>.24c mobile calls</li></ul><div class="sign">SIGNUP NOW</div></div>
  <div class="abs plan" style="left:277px"><h2>BUSINESS SAVER</h2><div class="price">$25<small> / month</small></div><ul><li>250 local calls included</li><li>.10c local calls</li><li>.22c mobile calls</li></ul><div class="sign">SIGNUP NOW</div></div>
  <div class="abs plan" style="left:469px"><h2>BUSINESS SUPER</h2><div class="price">$50<small> / month</small></div><ul><li>500 local calls included</li><li>.09c local calls</li><li>.20c mobile calls</li></ul><div class="sign">SIGNUP NOW</div></div>
  <div class="abs plan" style="left:661px"><h2>BUSINESS EXTREME</h2><div class="price">$100<small> / month</small></div><ul><li>1000 local calls included</li><li>.08c local calls</li><li>.18c mobile calls</li></ul><div class="sign">SIGNUP NOW</div></div>
</section>

<section class="abs features">
  <div class="feature">
    <div class="ic"><svg width="82" height="40" viewBox="0 0 82 40"><path d="M14 38a12 12 0 0 1 0-24 18 18 0 0 1 34-4 14 14 0 0 1 22 10 9 9 0 0 1 0 18z" fill="#333"/><path d="M28 26h20l-3-8H31z M30 16c3-3 13-3 16 0" fill="#fff" stroke="#fff" stroke-width="2"/></svg></div>
    <h3>HOSTED PBX</h3>
  </div>
  <div class="feature">
    <div class="ic"><svg width="46" height="46" viewBox="0 0 46 46"><rect x="2" y="2" width="12" height="40" rx="5" fill="#333"/><rect x="18" y="2" width="26" height="34" rx="4" fill="#333"/><g fill="#fff"><rect x="23" y="7" width="16" height="6"/><rect x="23" y="17" width="4" height="3"/><rect x="29" y="17" width="4" height="3"/><rect x="35" y="17" width="4" height="3"/><rect x="23" y="23" width="4" height="3"/><rect x="29" y="23" width="4" height="3"/><rect x="35" y="23" width="4" height="3"/></g></svg></div>
    <h3>PRANMOOR PHONES</h3>
  </div>
  <div class="feature">
    <div class="ic"><svg width="44" height="44" viewBox="0 0 44 44"><path d="M6 2h32l4 30H2z" fill="#333"/><rect x="2" y="32" width="40" height="10" fill="#333"/><g fill="#fff"><rect x="7" y="35" width="20" height="3"/><circle cx="36" cy="37" r="2"/></g></svg></div>
    <h3>KELSWITCH</h3>
  </div>
  <div class="feature">
    <div class="ic"><span class="wordmark">Dorvex</span></div>
    <h3>DORVEX</h3>
  </div>
</section>

<section class="about">
  <h2>Small to Medium Business Phone Systems &amp; Hosted PBX Solutions</h2>
  <p>Phasellus porta risus quis ligula fringilla, nec posuere magna eleifend. Phasellus congue, nisi a rhoncus consectetur, nibh ligula feugiat metus, id molestie erat enim in elit. Donec eu tempus risus. Nulla accumsan lacus nec rutrum aliquet. Nam quis suscipit ligula. Interdum et malesuada fames ac ante ipsum primis in faucibus. Phasellus ut metus eu lorem consect etur consectetur a quis leo. Cras sit amet tellus leo. Donec magna ante, congue ut nunc.</p>
  <div class="art" role="img" aria-label="Illustration of servers connected to a globe, laptops and phones in a network"></div>
</section>

<div class="abs band"></div>

<footer>
  <div class="abs fcol" style="left:86px;top:1000px"><h4>NAVIGATION</h4><ul><li>Home</li><li>About Us</li><li>Hosted PBX</li><li>Telephone Systems</li><li>Plans</li><li>Contact Us</li></ul></div>
  <div class="abs fcol" style="left:278px;top:1000px"><h4>PRODUCT CATEGORIES</h4><ul><li>IP Telephones</li><li>Conference Phone</li><li>Headsets</li><li>Switches</li><li>KelSwitch IP Telephone Systems</li><li>Dorvex Trellis</li><li>Dect Phones</li></ul></div>
  <div class="abs fcol" style="left:471px;top:1000px"><h4>HELPFUL LINKS</h4><ul><li>Plans &amp; Signup</li><li>Returns Policy</li><li>Terms and Privacy</li></ul></div>
  <div class="abs fcol" style="left:644px;top:1000px"><h4>CONNECT WITH US</h4>
    <div class="social"><b></b><b></b><b></b><b></b><b></b></div>
    <div class="contact">E-mail : sales@tellarovoice.com.au<br>Phone : 1300 482 917</div>
  </div>
  <div class="abs foot">Copyright © 2014 Tellaro Voice. All Rights Reserved</div>
</footer>

</body>
</html>
```